Industrial / automotive service company
Renewing and reconditioning solutions
Simple
Ted Pelkin
VP - Industrial Division
217 Marston Crescent NW
Calgary, Alberta
T2P 4G6
t-pelkin@zorvamail.com

```html
<!DOCTYPE html>
<html lang="en">
<head>
<meta charset="utf-8">
<title>Tovalmex Services Inc. – Business Card</title>
<link rel="stylesheet" href="https://fonts.googleapis.com/css2?family=Michroma&display=swap">
<style>
  :root {
    --green: #8cc63f;
    --green-dark: #7ab32f;
    --white: #ffffff;
    --paper: #f7f7f5;
    --ink: #5c5c5c;
    --backdrop: #e4e4e2;
  }
  * { margin: 0; padding: 0; box-sizing: border-box; }
  html, body {
    width: 1200px; height: 838px; overflow: hidden;
    background: var(--backdrop);
    font-family: "Michroma", sans-serif;
  }
  .canvas {
    position: relative; width: 1200px; height: 838px;
  }
  .card {
    position: absolute; width: 540px; height: 309px;
    box-shadow: 0 6px 18px rgba(0,0,0,0.18);
    overflow: hidden;
  }
  /* Front: contact side */
  .card-front { left: 40px; top: 264px; background: var(--paper); }
  .front-band {
    height: 70px; background: var(--green);
    display: flex; align-items: flex-end; justify-content: flex-end;
    padding: 0 34px 10px;
  }
  .holder {
    color: var(--white); font-size: 8px; letter-spacing: 0.06em;
    white-space: nowrap;
  }
  .holder .sep { margin: 0 6px; }
  .front-logo {
    position: absolute; left: 0; right: 0; top: 118px;
    display: flex; align-items: center; justify-content: center; gap: 10px;
  }
  .wordmark {
    color: var(--green); font-size: 20px; line-height: 1.15;
    letter-spacing: 0.04em; text-align: left;
  }
  .wordmark small { display: block; font-size: 10px; letter-spacing: 0.1em; }
  .mark-dot {
    width: 14px; height: 14px; border-radius: 50%; background: var(--green);
  }
  .contacts {
    position: absolute; left: 28px; right: 28px; bottom: 22px;
    display: grid; grid-template-columns: auto auto; row-gap: 8px; column-gap: 24px;
    color: var(--ink); font-size: 6.5px; letter-spacing: 0.05em;
  }
  .contact { display: flex; align-items: center; gap: 6px; white-space: nowrap; }
  .contact svg { width: 10px; height: 10px; flex: none; }
  /* Back: brand side */
  .card-back {
    left: 620px; top: 264px; background: var(--green);
    display: flex; align-items: center; justify-content: center; gap: 12px;
  }
  .card-back .wordmark { color: var(--white); font-size: 24px; }
  .card-back .wordmark small { font-size: 12px; }
  .card-back .mark-dot { background: var(--white); width: 16px; height: 16px; }
</style>
</head>
<body>
<main class="canvas">
  <section class="card card-front" aria-label="Business card, contact side">
    <div class="front-band">
      <p class="holder">TED PELKIN<span class="sep">|</span>VP<span class="sep">|</span>INDUSTRIAL DIVISION</p>
    </div>
    <div class="front-logo">
      <span class="mark-dot"></span>
      <p class="wordmark">TOVALMEX<small>SERVICES INC.</small></p>
    </div>
    <div class="contacts">
      <p class="contact">
        <svg viewBox="0 0 10 10"><circle cx="5" cy="5" r="5" fill="var(--green)"/><path d="M5 2.2a1.8 1.8 0 0 0-1.8 1.8c0 1.4 1.8 3.6 1.8 3.6s1.8-2.2 1.8-3.6A1.8 1.8 0 0 0 5 2.2z" fill="#fff"/></svg>
        217 MARSTON CRESCENT NW CALGARY, ALBERTA T2P 4G6
      </p>
      <p class="contact">
        <svg viewBox="0 0 10 10"><circle cx="5" cy="5" r="5" fill="var(--green)"/><path d="M3.3 2.5l1 1-.5.8a4 4 0 0 0 1.9 1.9l.8-.5 1 1-.6.8C5.4 7.3 2.7 4.6 2.5 3.1z" fill="#fff"/></svg>
        (403) 555-0148
      </p>
      <p class="contact">
        <svg viewBox="0 0 10 10"><circle cx="5" cy="5" r="5" fill="var(--green)"/><rect x="2.5" y="3.2" width="5" height="3.6" fill="#fff"/><path d="M2.5 3.2L5 5.2 7.5 3.2" fill="none" stroke="var(--green)" stroke-width=".6"/></svg>
        T-PELKIN@ZORVAMAIL.COM
      </p>
      <p class="contact">
        <svg viewBox="0 0 10 10"><circle cx="5" cy="5" r="5" fill="var(--green)"/><circle cx="5" cy="5" r="2.4" fill="none" stroke="#fff" stroke-width=".7"/><path d="M2.6 5h4.8M5 2.6v4.8" stroke="#fff" stroke-width=".5"/></svg>
        WWW.TOVALMEX.COM
      </p>
    </div>
  </section>

  <section class="card card-back" aria-label="Business card, brand side">
    <span class="mark-dot"></span>
    <p class="wordmark">TOVALMEX<small>SERVICES INC.</small></p>
  </section>
</main>
</body>
</html>
```